PowerPoint Corporate Template for Healthcare AI Technology Company

Take logo and create a comprehensive source file for corporate PowerPoint presentation library that provides an array of title/separator slides, graphic presentation options, chart options and text slide options. Utilize the current logo files and provide options on white backgrounds, and knock out options.

Target Market(s)

Pharmaceutical Manufacturers

Font styles to use
Sans Serif

Colors
6b449b
0556a4
33a6d7
0393ce
ffffff
e34197

Requirements
Must have
• Use logos upgraded in files; create an embedded color palette that aligns to the logo; include multiple options for different types of slides including charts; create a bullet point that is the logo in the purple/blue color with white background; incorporate knock out logo version option for separator pages; must include page numbers; use font aligned to logo for text slide options
Nice to have
• Tech looking, data intensive slide options that communicate easily; could be using 3-4 data points per slide
Should not have
• Any logo other than what has been shared

```html
<!DOCTYPE html>
<html lang="en">
<head>
<meta charset="utf-8">
<title>Veltrano – slide template library</title>
<link href="https://fonts.googleapis.com/css2?family=Arimo:wght@400&display=swap" rel="stylesheet">
<style>
  :root {
    --canvas: #ababab;
    --pink: #e34197;
    --purple: #6b449b;
    --navy: #0556a4;
    --sky: #0393ce;
    --sky-light: #33a6d7;
    --white: #ffffff;
    --ink: #111111;
    --grey-text: #555555;
    --grid: #d9d9d9;
  }
  * { margin: 0; padding: 0; box-sizing: border-box; }
  html, body { width: 1200px; height: 1200px; overflow: hidden; }
  body {
    background: var(--canvas);
    font-family: "Arimo", Arial, sans-serif;
    position: relative;
  }
  .slide {
    position: absolute;
    width: 551px;
    height: 310px;
    background: var(--white);
    overflow: hidden;
  }
  .slide--title { left: 33px; top: 278px; background: var(--pink); }
  .slide--pie { left: 616px; top: 278px; }
  .slide--bar { left: 33px; top: 613px; }
  .slide--info { left: 616px; top: 613px; }

  .title-mark {
    position: absolute; left: 25px; top: 133px;
    width: 60px; height: 60px; border-radius: 50%;
    border: 2px solid var(--white);
  }
  .title-heading {
    position: absolute; left: 101px; top: 149px;
    color: var(--white); font-size: 22px; letter-spacing: 0.2px;
    white-space: nowrap;
  }

  .brand {
    position: absolute; right: 19px; top: 17px;
    display: flex; align-items: center; gap: 6px;
    color: var(--purple); font-size: 26px; line-height: 1;
  }
  .brand-dot {
    width: 26px; height: 26px; border-radius: 50%;
    border: 2px solid var(--purple);
  }
  .header-rule {
    position: absolute; left: 0; width: 532px; top: 59px;
    height: 1px; background: var(--purple);
  }
  .slide-heading {
    position: absolute; left: 25px; top: 80px;
    color: var(--purple); font-size: 20px; white-space: nowrap;
  }
  .slide--bar .slide-heading { left: 24px; }

  .bullets {
    position: absolute; left: 25px; top: 136px;
    list-style: none; color: var(--ink); font-size: 16px; line-height: 23px;
  }
  .slide--bar .bullets { left: 24px; }
  .bullets li { white-space: nowrap; display: flex; align-items: center; }
  .bullets li::before {
    content: ""; width: 9px; height: 9px; border-radius: 50%;
    border: 1.5px solid var(--sky-light); margin: 0 7px 0 1px; flex: none;
  }
  .bullets li.sub { padding-left: 16px; line-height: 18px; }
  .bullets li.sub::before { display: none; }

  .footer-band {
    position: absolute; left: 0; bottom: 0; width: 100%; height: 24px;
    background: var(--purple);
  }
  .page-number {
    position: absolute; right: 22px; bottom: 7px;
    color: var(--white); font-size: 8px;
  }
  .chart { position: absolute; left: 0; top: 0; }
  .chart text { font-family: "Arimo", Arial, sans-serif; }
</style>
</head>
<body>

<section class="slide slide--title">
  <div class="title-mark"></div>
  <h1 class="title-heading">Veltrano – annual data reports</h1>
</section>

<section class="slide slide--pie">
  <div class="brand"><span class="brand-dot"></span>Veltrano</div>
  <div class="header-rule"></div>
  <h2 class="slide-heading">Pie chart data</h2>
  <ul class="bullets">
    <li>Lorem ipsum dolor sit amet</li>
    <li>Consectetur adipiscing elit</li>
    <li>Sed do eiusmod tempor incididunt</li>
    <li class="sub">- Ut labore et dolore magna aliqua</li>
    <li class="sub">- Laboris nisi ut aliquip ex ea</li>
    <li>Commodo consequat</li>
  </ul>
  <svg class="chart" width="551" height="310" viewBox="0 0 551 310">
    <g transform="rotate(-90 442 164)" fill="none" stroke-width="44">
      <circle cx="442" cy="164" r="66" stroke="var(--pink)" stroke-dasharray="242.9 414.7"/>
      <circle cx="442" cy="164" r="66" stroke="var(--purple)" stroke-dasharray="0 242.9 94.8 414.7"/>
      <circle cx="442" cy="164" r="66" stroke="var(--navy)" stroke-dasharray="0 337.7 41.5 414.7"/>
      <circle cx="442" cy="164" r="66" stroke="var(--sky)" stroke-dasharray="0 379.2 35.5 414.7"/>
    </g>
    <g stroke="var(--white)" stroke-width="1.2">
      <line x1="442" y1="164" x2="442" y2="76"/>
      <line x1="442" y1="164" x2="396" y2="239"/>
      <line x1="442" y1="164" x2="362" y2="127"/>
      <line x1="442" y1="164" x2="397" y2="88"/>
    </g>
    <text x="441" y="168" text-anchor="middle" font-size="10" fill="var(--grey-text)">Sales</text>
    <g font-size="6.5" fill="var(--grey-text)">
      <rect x="380" y="262" width="3" height="3" fill="var(--pink)"/><text x="385" y="265.5">1st Qtr</text>
      <rect x="412" y="262" width="3" height="3" fill="var(--purple)"/><text x="417" y="265.5">2nd Qtr</text>
      <rect x="446" y="262" width="3" height="3" fill="var(--navy)"/><text x="451" y="265.5">3rd Qtr</text>
      <rect x="479" y="262" width="3" height="3" fill="var(--sky)"/><text x="484" y="265.5">4th Qtr</text>
    </g>
  </svg>
  <div class="footer-band"></div>
  <span class="page-number">6</span>
</section>

<section class="slide slide--bar">
  <div class="brand"><span class="brand-dot"></span>Veltrano</div>
  <div class="header-rule"></div>
  <h2 class="slide-heading">Bar chart data</h2>
  <ul class="bullets">
    <li>Lorem ipsum dolor sit amet</li>
    <li>Consectetur adipiscing elit</li>
    <li>Sed do eiusmod tempor incididunt</li>
    <li class="sub">- Ut labore et dolore magna aliqua</li>
    <li class="sub">- Laboris nisi ut aliquip ex ea</li>
    <li>Commodo consequat</li>
  </ul>
  <svg class="chart" width="551" height="310" viewBox="0 0 551 310">
    <text x="420" y="87" text-anchor="middle" font-size="10" fill="var(--grey-text)">Sales</text>
    <g stroke="var(--grid)" stroke-width="0.7">
      <line x1="335" y1="96" x2="335" y2="244"/>
      <line x1="373.6" y1="96" x2="373.6" y2="244"/>
      <line x1="412.2" y1="96" x2="412.2" y2="244"/>
      <line x1="450.8" y1="96" x2="450.8" y2="244"/>
      <line x1="489.4" y1="96" x2="489.4" y2="244"/>
      <line x1="528" y1="96" x2="528" y2="244"/>
    </g>
    <rect x="336" y="105.5" width="23" height="17" fill="var(--sky)"/>
    <rect x="336" y="142.5" width="27" height="17" fill="var(--navy)"/>
    <rect x="336" y="178.5" width="61" height="17" fill="var(--purple)"/>
    <rect x="336" y="215.5" width="158" height="17" fill="var(--pink)"/>
    <g font-size="6.5" fill="var(--grey-text)" text-anchor="end">
      <text x="329" y="116.5">4th Qtr</text>
      <text x="329" y="153.5">3rd Qtr</text>
      <text x="329" y="189.5">2nd Qtr</text>
      <text x="329" y="226.5">1st Qtr</text>
    </g>
    <g font-size="6.5" fill="var(--grey-text)" text-anchor="middle">
      <text x="335" y="253">0</text>
      <text x="373.6" y="253">2</text>
      <text x="412.2" y="253">4</text>
      <text x="450.8" y="253">6</text>
      <text x="489.4" y="253">8</text>
      <text x="528" y="253">10</text>
    </g>
    <g font-size="6.5" fill="var(--grey-text)">
      <rect x="359" y="262" width="3" height="3" fill="var(--pink)"/><text x="364" y="265.5">1st Qtr</text>
      <rect x="391" y="262" width="3" height="3" fill="var(--purple)"/><text x="396" y="265.5">2nd Qtr</text>
      <rect x="426" y="262" width="3" height="3" fill="var(--navy)"/><text x="431" y="265.5">3rd Qtr</text>
      <rect x="459" y="262" width="3" height="3" fill="var(--sky)"/><text x="464" y="265.5">4th Qtr</text>
    </g>
  </svg>
  <div class="footer-band"></div>
  <span class="page-number">7</span>
</section>

<section class="slide slide--info">
  <div class="brand"><span class="brand-dot"></span>Veltrano</div>
  <div class="header-rule"></div>
  <h2 class="slide-heading">Information</h2>
  <ul class="bullets">
    <li>Lorem ipsum dolor</li>
    <li>Consectetur adipiscing</li>
    <li>Sed do eiusmod tempor</li>
    <li>Commodo consequat</li>
  </ul>
  <svg class="chart" width="551" height="310" viewBox="0 0 551 310">
    <defs>
      <linearGradient id="photo-desk" x1="0" y1="0" x2="1" y2="1">
        <stop offset="0" stop-color="#c9b49a"/><stop offset="1" stop-color="#6fa6cf"/>
      </linearGradient>
      <linearGradient id="photo-tech" x1="0" y1="0" x2="1" y2="1">
        <stop offset="0" stop-color="#0a2a3a"/><stop offset="1" stop-color="#1f6f8f"/>
      </linearGradient>
      <linearGradient id="photo-office" x1="0" y1="0" x2="0" y2="1">
        <stop offset="0" stop-color="#cfe6f3"/><stop offset="1" stop-color="#1a7fb8"/>
      </linearGradient>
      <polygon id="hex" points="-40,0 -20,-35 20,-35 40,0 20,35 -20,35"/>
    </defs>
    <use href="#hex" x="419" y="111" fill="url(#photo-desk)" role="img" aria-label="Photo of a desk with a calculator and printed financial charts"/>
    <use href="#hex" x="279" y="188" fill="url(#photo-tech)" role="img" aria-label="Photo of a hand touching a glowing digital interface"/>
    <use href="#hex" x="487" y="225" fill="url(#photo-office)" role="img" aria-label="Photo of business people in a bright glass meeting room"/>
    <use href="#hex" x="348" y="149" fill="var(--purple)"/>
    <use href="#hex" x="417" y="187" fill="var(--pink)"/>
    <use href="#hex" x="348" y="225" fill="var(--sky)"/>
    <g font-size="14" fill="var(--white)" text-anchor="middle">
      <text x="348" y="154">Title 1</text>
      <text x="417" y="192">Title 2</text>
      <text x="348" y="230">Title 3</text>
    </g>
  </svg>
  <div class="footer-band"></div>
  <span class="page-number">8</span>
</section>

</body>
</html>
```